Dodgeball League website

I require a nice, cool and attractive website for a new dodgeball league competition. I will need in PSD:

- Home Page
- Generic pages for news, about us etc
- Rank page with a table of team scores. stats etc

*Please design this with a Joomla*

I have attached:
- a logo
- site map for the links
- page layout guide

Example site for layout
http://www.velmorcircuit.com/

Design
Retro,cool feel, matches well with logo

Contact me if you have any questions

Reason: Would like to see a few more designs

Target Market(s)

Young adults 18 - 35.

Industry/Entity Type

News

Colors

Designer to choose colors to be used in the design.

Requirements
Must have
• I want a cool, retro feel to the website. Not to picky on the colors. Something that will match nicely with the logo given. I will give feedback on it.
Calm colors not too bright and overwhelming
Nice to have
• Include some pictures within the picture slider so I can get a feel for the website.
Nice clean background
Should not have
• To much clutter of text
Do not put pictures in the background.

```html
<!DOCTYPE html>
<html lang="en">
<head>
<meta charset="utf-8">
<title>Crossline Dodgeball League</title>
<link href="https://fonts.googleapis.com/css2?family=Open+Sans:wght@400;600;700&display=swap" rel="stylesheet">
<style>
:root{
  --red:#9a1f16;--red-dark:#6e130d;--red-btn:#c21a12;--gold:#f6c531;--gold-deep:#e8a817;
  --tan:#ecd6ac;--tan-dark:#b88a4e;--ink:#111;--paper:#f2f2f0;--orange:#c0391b;--peach:#f6a77c;
  --grey:#4a4a4a;--link:#d0401f;--blue:#3b5998;
}
*{box-sizing:border-box;margin:0;padding:0}
html,body{width:906px;height:1200px;overflow:hidden}
body{background:var(--paper);font-family:"Open Sans",sans-serif;color:var(--ink);position:relative}
.abs{position:absolute}
.header{left:74px;top:4px;width:755px;height:108px;background:var(--red)}
.brand{left:80px;top:8px;width:124px;height:100px;display:flex;align-items:center;gap:6px}
.brand .dot{width:22px;height:22px;border-radius:50%;background:var(--gold);flex:none}
.brand span{font-weight:700;font-size:13px;color:var(--gold);line-height:1.15}
.scorebox{top:10px;width:195px;height:96px;background:#f3ead6}
.scorebox .tabs{height:18px;background:var(--red-dark);display:flex;justify-content:space-around;align-items:center;font-size:8px;font-weight:700;color:var(--gold)}
.scorebox .heads{font-size:8px;color:var(--link);font-weight:600;height:14px;position:relative}
.scorebox .heads b{position:absolute;top:2px;font-weight:600}
.scorebox .row{position:relative;margin:3px 3px 0;height:22px;background:var(--ink);color:#fff;font-size:8px;font-weight:600;display:flex;align-items:center;padding-left:8px}
.scorebox .row + .row{margin-top:5px}
.scorebox .row i{position:absolute;top:3px;width:12px;height:16px;background:#fff;color:var(--ink);font-style:normal;text-align:center;line-height:16px}
.next{left:809px;top:50px}
.nav{left:74px;top:120px;width:755px;height:30px;background:linear-gradient(#6b2410,#4d1808);display:flex;align-items:center;justify-content:space-between;padding:0 16px;font-size:12.5px;color:#fff}
.nav .active{color:var(--gold)}
.nav .dd::after{content:"";display:inline-block;margin-left:6px;border:4px solid transparent;border-top-color:var(--gold);vertical-align:-2px}
.slider{left:75px;top:159px;width:754px;height:304px;background:linear-gradient(180deg,#3a4a78 0%,#5a6a9a 45%,#2f54a8 80%,#222 100%)}
.slider .cap{position:absolute;left:16px;top:182px;color:#fff}
.slider h1{font-size:24px;font-weight:600;letter-spacing:.5px}
.slider p{font-size:11.5px;line-height:16px;width:330px}
.btn-dark{display:inline-block;background:#111;color:var(--gold);font-size:9px;font-weight:600;padding:4px 13px;margin:6px 6px 0 0}
.slider .band{position:absolute;left:0;bottom:0;width:100%;height:26px;background:rgba(0,0,0,.45)}
.arrow{position:absolute;top:134px;width:38px;height:38px;border-radius:50%;background:rgba(230,230,230,.85)}
.pager{position:absolute;right:14px;bottom:8px;display:flex;gap:6px}
.pager i{width:9px;height:9px;background:#fff}
.pager i:first-child{background:var(--gold)}
.hl-bar{left:78px;top:472px;width:490px;height:50px;background:var(--ink);display:flex;align-items:center;color:#fff}
.hl-bar .mark{width:70px;height:60px;margin-top:-6px;display:flex;align-items:center;justify-content:center}
.hl-bar .mark i{width:46px;height:46px;border-radius:50%;background:var(--gold)}
.hl-bar h2{font-size:14px;font-weight:700;flex:1}
.watch{background:var(--red-btn);color:#fff;font-size:14px;font-weight:600;width:140px;height:27px;line-height:27px;text-align:center;margin-right:12px}
.hl-body{left:78px;top:528px;width:486px;height:142px;background:var(--tan)}
.hl-photo{left:91px;top:545px;width:107px;height:107px;background:linear-gradient(135deg,#3b5fa8,#d7cbb8 60%,#8a6a9a)}
.hl-main{left:203px;top:542px;width:145px;font-size:8.5px;color:#444;line-height:13.5px}
.hl-main h3{font-size:11.5px;color:var(--link);font-weight:600;margin-bottom:4px}
.hl-main .date{font-size:9px;color:var(--ink);margin-bottom:6px}
.hl-main .more{color:var(--ink);font-size:9px;margin-top:6px}
.hl-list{left:362px;top:530px;width:190px;font-size:8.5px;list-style:none}
.hl-list li{height:18.2px;line-height:18px;border-bottom:1px solid #d6b987;white-space:nowrap;overflow:hidden}
.hl-list li b{font-weight:400;color:var(--ink);margin-right:2px}
.hl-list li span{color:var(--link)}
.viewall{left:516px;top:657px;font-size:9px}
.fan{left:577px;top:470px;width:252px;height:96px;background:#eae8e4;border:1px solid #d4d0c8}
.fan .mark{position:absolute;left:10px;top:16px;width:60px;height:60px;border-radius:50%;background:var(--gold)}
.fan h4{position:absolute;left:98px;top:18px;font-size:14px;font-weight:700;line-height:17px}
.likebtn{position:absolute;left:162px;top:52px;width:78px;border:1px solid #c6c6c6;background:#f5f5f5;color:var(--blue);padding:3px 6px;font-weight:600;line-height:10px;white-space:nowrap}
.likebtn small{display:block;font-size:6.5px}
.likebtn span{font-size:10px;line-height:12px}
.reg{left:577px;top:576px;width:252px;height:96px;background:#5b3b1f}
.reg h4{height:27px;background:var(--ink);color:#fff;font-size:14px;font-weight:600;padding:4px 8px}
.field{position:absolute;left:10px;height:18px;background:#fff;font-size:9px;color:#aaa;padding:3px 6px}
.submit{position:absolute;left:159px;top:65px;width:83px;height:18px;background:var(--red-btn);color:#fff;font-size:10px;font-weight:600;text-align:center;line-height:18px}
.league{left:76px;top:682px;width:490px;height:238px;background:#e6e2dc;border:1px solid #ccc}
.league .tabs{position:absolute;left:5px;top:5px;width:480px;height:34px;display:flex;background:var(--ink);color:#fff;font-size:14.5px;font-weight:600}
.league .tabs div{flex:1;display:flex;align-items:center;justify-content:center}
.league .tabs div + div{border-left:2px solid #fff}
.rt{position:absolute;left:6px;top:42px;width:479px;border-collapse:separate;border-spacing:0 3px;font-size:12px}
.rt td,.rt th{height:24px;font-weight:600}
.rt th{height:25px;font-weight:400;font-size:12.5px}
.rt .rk{width:64px;background:var(--red);color:#fff;text-align:center;border-right:3px solid #e6e2dc}
.rt th.rk{background:var(--orange)}
.rt .tm{background:var(--gold);color:#7a2a12;padding-left:11px;border-right:3px solid #e6e2dc}
.rt th.tm{color:#222;text-align:left}
.rt .sc{width:76px;background:var(--peach);color:#fff;text-align:center}
.rt th.sc{background:var(--gold);color:#222}
.connect{left:577px;top:682px;width:252px;height:160px;background:#f1f0ee;border:1px solid #ccc}
.connect h4{position:absolute;left:9px;top:8px;font-size:12.5px;color:var(--red);font-weight:600}
.connect .mark{position:absolute;left:12px;top:32px;width:46px;height:46px;border-radius:50%;background:var(--gold)}
.connect .pg{position:absolute;left:65px;top:32px;color:var(--blue);font-size:12px;font-weight:600}
.connect .lk{position:absolute;left:67px;top:52px;border:1px solid #bbb;font-size:8px;color:var(--blue);padding:1px 4px}
.connect .cnt{position:absolute;left:14px;top:84px;font-size:7.5px;color:#333}
.connect .cnt span{color:var(--blue)}
.faces{position:absolute;left:14px;top:98px;width:218px;height:34px;background:linear-gradient(90deg,#b6a48c,#4a3c36,#b88,#333,#c77)}
.connect .plug{position:absolute;left:14px;top:146px;font-size:7px;color:#555}
.map{left:577px;top:854px;width:252px;height:68px;background:linear-gradient(120deg,#cfe3b4,#efe9dc 55%,#d9e6c6)}
.tops{left:74px;top:930px;width:755px;height:110px;background:var(--tan)}
.top3{position:absolute;top:937px;width:241px;height:96px;font-size:8.5px}
.top3 h5{height:25px;font-size:12px;font-weight:700;padding:4px 7px}
.top3 .hd,.top3 .r{display:flex;padding:0 8px}
.top3 .hd{height:20px;align-items:center;font-size:8.5px}
.top3 .r{height:14.5px;align-items:center}
.top3 .a{width:44px}.top3 .b{flex:1}.top3 .c{width:32px;text-align:right}
.t-red{background:var(--red)}.t-red h5{background:var(--gold)}.t-red .hd{color:#fff}.t-red .r{color:var(--peach)}
.t-grey{background:var(--grey);color:#fff}.t-grey h5{background:var(--ink)}
.t-black{background:var(--ink);color:#fff}.t-black h5{background:var(--red)}
.partners{left:74px;top:1048px;width:755px;height:112px;background:linear-gradient(90deg,#7a3a14,#e1c08a 12%,#f2dfb6 50%,#e1c08a 88%,#7a3a14);display:flex;align-items:center;justify-content:space-around;padding:0 6px}
.badge{background:#f7f3ea}
.footer{left:0;top:1174px;width:906px;text-align:center;font-size:9px;color:#555}
</style>
</head>
<body>

<div class="abs header"></div>
<div class="abs brand"><i class="dot"></i><span>Crossline Dodgeball League</span></div>

<div class="abs scorebox" style="left:210px">
  <div class="tabs"><span>» LIVE STREAM</span><span>» LIVE SCORES</span></div>
  <div class="heads"><b style="left:118px">Pts</b><b style="left:158px">Sets</b></div>
  <div class="row">Team 1 &nbsp;&nbsp; 10<i style="left:147px">2</i><i style="left:162px">2</i></div>
  <div class="row">Team 2 &nbsp;&nbsp; 5<i style="left:147px">6</i><i style="left:162px">6</i></div>
</div>
<div class="abs scorebox" style="left:408px">
  <div class="tabs"><span>» LIVE STREAM</span><span>» LIVE SCORES</span></div>
  <div class="heads"><b style="left:118px">Pts</b><b style="left:158px">Sets</b></div>
  <div class="row">Team 1 &nbsp;&nbsp; 10<i style="left:147px">2</i><i style="left:162px">2</i></div>
  <div class="row">Team 2 &nbsp;&nbsp; 5<i style="left:147px">6</i><i style="left:162px">6</i></div>
</div>
<div class="abs scorebox" style="left:607px">
  <div class="tabs"><span>» LIVE STREAM</span><span>» LIVE SCORES</span></div>
  <div class="heads"><b style="left:118px">Pts</b><b style="left:158px">Sets</b></div>
  <div class="row">Team 1 &nbsp;&nbsp; 10<i style="left:147px">2</i><i style="left:162px">2</i></div>
  <div class="row">Team 2 &nbsp;&nbsp; 5<i style="left:147px">6</i><i style="left:162px">6</i></div>
</div>
<svg class="abs next" width="14" height="22" viewBox="0 0 14 22"><path d="M2 2l9 9-9 9" fill="none" stroke="#f6c531" stroke-width="4"/></svg>

<nav class="abs nav">
  <span class="active">Home</span><span>About</span><span class="dd">Teams</span><span class="dd">Schedule</span><span class="dd">News</span><span class="dd">Photos and Videos</span><span>Register</span><span>Contact Us</span>
</nav>

<section class="abs slider" role="img" aria-label="Dodgeball player throwing a ball in front of seated teams">
  <div class="arrow" style="left:16px"><svg width="38" height="38"><path d="M22 11l-8 8 8 8" fill="none" stroke="#333" stroke-width="4"/></svg></div>
  <div class="arrow" style="right:14px"><svg width="38" height="38"><path d="M16 11l8 8-8 8" fill="none" stroke="#333" stroke-width="4"/></svg></div>
  <div class="cap">
    <h1>GLOSS ON THE FINISH</h1>
    <p>Marco Varell is looking to cap a dream comeback in 2013 with his final two tournaments in Paris and London.</p>
    <span class="btn-dark">Read More</span><span class="btn-dark">Watch Live</span>
  </div>
  <div class="band"></div>
  <div class="pager"><i></i><i></i><i></i><i></i></div>
</section>

<div class="abs hl-bar"><div class="mark"><i></i></div><h2>DODGEBALL LEAGUE HEADLINES</h2><div class="watch">Watch Live</div></div>
<div class="abs hl-body"></div>
<div class="abs hl-photo" role="img" aria-label="Players diving for dodgeballs on court"></div>
<div class="abs hl-main">
  <h3>Sed ut perspiciatis</h3>
  <div class="date">29-09-2013</div>
  Sed ut perspiciatis und.e omnis iste natus error sit voluptatem accusantiu doloremque laudanti, totam rem aperiam.
  <div class="more">Read More</div>
</div>
<ul class="abs hl-list">
  <li><b>29.10</b> <span>Paris Tuesday Preview: Halvorsen,</span></li>
  <li><b>28.10</b> <span>Varell Looking To Put The Gloss</span></li>
  <li><b>28.10</b> <span>VTC Challenger Tour Finals Field Set</span></li>
  <li><b>28.10</b> <span>London Contenders To Face</span></li>
  <li><b>28.10</b> <span>Paris Monday Preview: Varell, Halvorsen</span></li>
  <li><b>27.10</b> <span>Harbor VTC Weekly Slice: Three</span></li>
  <li><b>27.10</b> <span>Castellan Retains Basel Title; Lindqvist's</span></li>
</ul>
<div class="abs viewall">View All</div>

<div class="abs fan"><i class="mark"></i><h4>Crossline Dodgeball League</h4><div class="likebtn"><small>Like us on</small><span>Socialhub</span></div></div>

<div class="abs reg">
  <h4>Register Here</h4>
  <div class="field" style="top:37px;width:232px">Enter Your Name</div>
  <div class="field" style="top:65px;width:149px">Enter Your Email</div>
  <div class="submit">Submit</div>
</div>

<section class="abs league">
  <div class="tabs"><div>Ultimate Rubber League</div><div>Ultimate Foam League</div></div>
  <table class="rt">
    <tr><th class="rk">Rank</th><th class="tm">Team</th><th class="sc">Score</th></tr>
    <tr><td class="rk">1</td><td class="tm">Sed ut perspiciatis unde omnis iste natus</td><td class="sc">24</td></tr>
    <tr><td class="rk">2</td><td class="tm">Error sit voluptatem accusantium doloremque</td><td class="sc">36</td></tr>
    <tr><td class="rk">3</td><td class="tm">Laudantium, totam rem aperiam, eaque ipsa quae ab</td><td class="sc">25</td></tr>
    <tr><td class="rk">4</td><td class="tm">Illo inventore veritatis et quasi architecto beatae vitae</td><td class="sc">26</td></tr>
    <tr><td class="rk">5</td><td class="tm">Dicta sunt explicabo. Nemo enim ipsam voluptatem</td><td class="sc">27</td></tr>
    <tr><td class="rk">6</td><td class="tm">Quia voluptas sit aspernatur aut odit aut fugit, sed</td><td class="sc">30</td></tr>
  </table>
</section>

<section class="abs connect">
  <h4>Connect with Dodgeball League</h4>
  <i class="mark"></i>
  <div class="pg">Dodgeball League</div>
  <div class="lk">Like</div>
  <div class="cnt">4,637,331 people like <span>Dodgeball League</span></div>
  <div class="faces" role="img" aria-label="Row of fan profile photos"></div>
  <div class="plug">Socialhub social plugin</div>
</section>
<div class="abs map" role="img" aria-label="Street map of central London with a location pin"></div>

<div class="abs tops"></div>
<div class="top3 t-red" style="left:82px">
  <h5>TOP 3 KILLER</h5>
  <div class="hd"><span class="a">Rank</span><span class="b">Team</span><span class="c">Score</span></div>
  <div class="r"><span class="a">8</span><span class="b">Sed ut perspiciatis unde omnis</span><span class="c">3150</span></div>
  <div class="r"><span class="a">14</span><span class="b">iste natus error sit voluptatem</span><span class="c">2135</span></div>
  <div class="r"><span class="a">29</span><span class="b">accusantium doloremque</span><span class="c">1234</span></div>
</div>
<div class="top3 t-grey" style="left:331px">
  <h5>TOP 3 Catcher</h5>
  <div class="hd"><span class="a">Rank</span><span class="b">Team</span><span class="c">Score</span></div>
  <div class="r"><span class="a">8</span><span class="b">Sed ut perspiciatis unde omnis</span><span class="c">3150</span></div>
  <div class="r"><span class="a">14</span><span class="b">iste natus error sit voluptatem</span><span class="c">2135</span></div>
  <div class="r"><span class="a">29</span><span class="b">accusantium doloremque</span><span class="c">1234</span></div>
</div>
<div class="top3 t-black" style="left:579px">
  <h5>TOP 3 Dodger</h5>
  <div class="hd"><span class="a">Rank</span><span class="b">Team</span><span class="c">Score</span></div>
  <div class="r"><span class="a">8</span><span class="b">Sed ut perspiciatis unde omnis</span><span class="c">3150</span></div>
  <div class="r"><span class="a">14</span><span class="b">iste natus error sit voluptatem</span><span class="c">2135</span></div>
  <div class="r"><span class="a">29</span><span class="b">accusantium doloremque</span><span class="c">1234</span></div>
</div>

<section class="abs partners" aria-label="Partner leagues">
  <div class="badge" style="width:126px;height:94px;background:#ddd"></div>
  <div class="badge" style="width:76px;height:76px"></div>
  <div class="badge" style="width:70px;height:70px;border-radius:50%;background:#c8321e"></div>
  <div class="badge" style="width:88px;height:60px;background:#333"></div>
  <div class="badge" style="width:98px;height:66px;background:#e9b73a"></div>
  <div class="badge" style="width:78px;height:78px;border-radius:50%;background:#222"></div>
</section>

<div class="abs footer">© 2013 Crossline Dodgeball League, Inc. All rights reserved.</div>
</body>
</html>
```